Commercial facility maintenance

I need a card design that helps my salesmen make contact with new clients, our product is facility maintenance and heavy industrial maintenance

```html
<!DOCTYPE html>
<html lang="en">
<head>
<meta charset="UTF-8">
<title>Harlow Mechanical LLC. – Business Card</title>
<link rel="stylesheet" href="https://fonts.googleapis.com/css2?family=Montserrat:wght@400;500;600;700&display=swap">
<style>
  :root {
    --page-bg: #e6e2dd;
    --card-dark: #1b1b1c;
    --card-dark-edge: #2b2b2c;
    --card-light: #eee6da;
    --brand-red: #b3232b;
    --text-light: #d9cfc2;
    --text-muted: #c9bfb2;
    --ink: #2e2e30;
  }
  * { box-sizing: border-box; margin: 0; padding: 0; }
  html, body {
    width: 1200px;
    height: 1047px;
    overflow: hidden;
  }
  body {
    background: var(--page-bg);
    font-family: "Montserrat", sans-serif;
    position: relative;
  }
  .business-card {
    position: absolute;
    left: 100px;
    top: 250px;
    width: 1000px;
    height: 548px;
    border-radius: 20px;
    overflow: hidden;
    background: var(--card-light);
    box-shadow: 0 12px 36px rgba(0,0,0,0.18);
  }
  .card-background {
    position: absolute;
    inset: 0;
  }
  .brand-lockup {
    position: absolute;
    left: 43px;
    top: 48px;
    display: flex;
    align-items: center;
    gap: 14px;
  }
  .brand-lockup .brand-dot {
    width: 62px;
    height: 62px;
    border-radius: 50%;
    background: var(--brand-red);
  }
  .brand-lockup .brand-name {
    font-weight: 600;
    font-size: 26px;
    line-height: 1.15;
    letter-spacing: 1.5px;
    color: var(--text-muted);
    text-transform: uppercase;
  }
  .contact-block {
    position: absolute;
    left: 39px;
    top: 212px;
    color: var(--text-light);
  }
  .person-name {
    font-weight: 600;
    font-size: 39px;
    letter-spacing: 1px;
    color: var(--brand-red);
    line-height: 1;
  }
  .person-role {
    margin-top: 14px;
    font-size: 22px;
    letter-spacing: 0.5px;
  }
  .address {
    margin-top: 30px;
    font-size: 22px;
    line-height: 37px;
    letter-spacing: 0.5px;
  }
  .contact-list {
    list-style: none;
    margin-top: 20px;
  }
  .contact-list li {
    display: flex;
    align-items: center;
    gap: 9px;
    font-size: 21px;
    height: 37px;
    letter-spacing: 0.4px;
  }
  .contact-list svg {
    width: 16px;
    height: 16px;
    fill: var(--brand-red);
    flex: none;
  }
  .emblem-name {
    position: absolute;
    left: 539px;
    top: 69px;
    width: 410px;
    height: 410px;
    border-radius: 50%;
    border: 4px solid var(--ink);
    display: flex;
    flex-direction: column;
    align-items: center;
    justify-content: center;
    text-align: center;
    color: var(--ink);
    font-weight: 700;
    text-transform: uppercase;
  }
  .emblem-name .emblem-line-main {
    font-size: 62px;
    letter-spacing: 3px;
    line-height: 1.05;
  }
  .emblem-name .emblem-line-sub {
    font-size: 30px;
    letter-spacing: 3px;
    line-height: 1.3;
  }
</style>
</head>
<body>
  <article class="business-card">
    <svg class="card-background" width="1000" height="548" viewBox="0 0 1000 548" aria-hidden="true">
      <defs>
        <linearGradient id="darkPanel" x1="0" y1="0" x2="1" y2="1">
          <stop offset="0" stop-color="var(--card-dark-edge)"/>
          <stop offset="0.6" stop-color="var(--card-dark)"/>
          <stop offset="1" stop-color="#111112"/>
        </linearGradient>
      </defs>
      <path class="dark-panel" d="M0 0 H636 A305 305 0 0 0 636 548 H0 Z" fill="url(#darkPanel)"/>
      <path class="accent-arc" d="M636 0 A305 305 0 0 0 636 548 H680 A296 296 0 0 1 680 0 Z" fill="var(--brand-red)"/>
    </svg>

    <div class="brand-lockup">
      <span class="brand-dot"></span>
      <span class="brand-name">Harlow<br>Mechanical LLC.</span>
    </div>

    <section class="contact-block">
      <h1 class="person-name">DANIEL HART</h1>
      <p class="person-role">Managing Director</p>
      <p class="address">Your address, City<br>State, Zip 1234</p>
      <ul class="contact-list">
        <li>
          <svg viewBox="0 0 16 16"><path d="M2 5c0-1.5 1.3-2.5 2.5-2.5h7C12.7 2.5 14 3.5 14 5v1.2c0 .5-.4.8-.9.8h-2c-.5 0-.9-.3-.9-.8V5.5H5.8v.7c0 .5-.4.8-.9.8h-2C2.4 7 2 6.7 2 6.2z M4 8.5h8l1.5 5h-11z"/></svg>
          555-014-2290
        </li>
        <li>
          <svg viewBox="0 0 16 16"><path d="M1.5 3.5h13v9h-13z M2.5 4.5 8 9l5.5-4.5" stroke="#1b1b1c" stroke-width="1"/></svg>
          info@harlowmechanicalllc.com
        </li>
        <li>
          <svg viewBox="0 0 16 16"><circle cx="8" cy="8" r="6.5"/><path d="M5 4.5c1.5.5 2 1.5 1 2.5s.5 2 1.5 2.5-.5 2.5 0 3.5M10.5 3.5c-.5 1 .5 2 1.5 2" stroke="#1b1b1c" stroke-width="1" fill="none"/></svg>
          harlowmechanicalllc.com
        </li>
      </ul>
    </section>

    <div class="emblem-name">
      <span class="emblem-line-main">Harlow</span>
      <span class="emblem-line-sub">Mechanical LLC.</span>
    </div>
  </article>
</body>
</html>
```